Moodvane - Landing Page

Need a landing page for a journal app. The app is based on a retrospective board, where each journal entry is split into 3 sections: "What went well", "What Didn't Go Well" and "Things To Try".
The landing page should match the style of all modern web application landing pages. Think Plumo, Vexora, Zenquil. I've included screenshots of the app.
One feature that I want to highlight that is not ready yet, is an AI coach. It will offer insights based on the history of the user's journal entries
1 page

```html
<!DOCTYPE html>
<html lang="en">
<head>
<meta charset="utf-8">
<title>Moodvane – Reflect, Grow, and Succeed</title>
<link rel="stylesheet" href="https://fonts.googleapis.com/css2?family=Lexend:wght@300;400;500;600&family=Inter:wght@400;500;600;700&display=swap">
<style>
:root{
  --page:#f4f7fc;
  --navy:#0a2f8f;
  --royal:#0c47b0;
  --blue:#0c4aa6;
  --sky:#1a84cb;
  --soft-blue:#8bb2e2;
  --lime:#a6e43a;
  --ink:#17203a;
  --muted:#6d7486;
  --line:#dfe4ee;
  --white:#ffffff;
}
*{box-sizing:border-box;margin:0;padding:0}
html,body{width:1200px;height:4104px;overflow:hidden}
body{background:var(--page);font-family:"Inter",sans-serif;color:var(--ink);position:relative}
.abs{position:absolute}
.display{font-family:"Lexend",sans-serif;letter-spacing:-0.04em}
.swoosh{position:absolute;left:0;width:100%;height:14px;overflow:visible}

/* Hero */
.hero{position:absolute;left:35px;top:35px;width:1130px;height:782px;border-radius:4px 40px 4px 4px;overflow:hidden;
  background:linear-gradient(120deg,#0a2a86 0%,#0b3ca6 55%,#0a4fb8 100%)}
.brand{position:absolute;left:53px;top:16px;display:flex;flex-direction:column;align-items:center;gap:6px}
.brand-mark{width:30px;height:30px;border-radius:6px;background:var(--lime)}
.brand-name{font-family:"Lexend",sans-serif;font-weight:600;font-size:22px;color:var(--white);letter-spacing:-0.02em}
.nav{position:absolute;top:36px;left:231px;display:flex;gap:0;font-size:12px;color:var(--white);font-weight:500}
.nav span{position:absolute;white-space:nowrap}
.btn-login{position:absolute;left:601px;top:22px;width:67px;height:30px;background:#1f5dc6;color:#fff;font-size:11px;font-weight:700;display:flex;align-items:center;justify-content:center;border-radius:3px}
.btn-signup{position:absolute;left:682px;top:30px;color:#fff;font-size:11px;font-weight:700}
.hero-title{position:absolute;left:50px;top:232px;font-size:62px;line-height:58px;color:var(--white);font-weight:500}
.hero-title .faint{color:#9fb5dc}
.hero-sub{position:absolute;left:53px;top:440px;width:305px;font-size:14px;line-height:22px;color:#e4ebfa}
.hero-disc{position:absolute;left:56px;top:614px;width:137px;height:143px;border-radius:50%;
  background:radial-gradient(circle at 65% 35%,#a9c8f2 0%,#4f86d8 45%,#1d4fb0 100%);opacity:.85}

/* Mockup */
.mock{position:absolute;left:420px;top:190px;width:1020px;height:640px;transform:rotate(-14deg);transform-origin:0 0;
  background:#f5f7fb;border-radius:18px;box-shadow:0 30px 60px rgba(0,0,30,.35);overflow:hidden}
.mock-side{position:absolute;left:0;top:0;width:62px;height:100%;background:#1d2740}
.mock-side i{position:absolute;left:20px;width:20px;height:14px;border:2px solid #c8d0e0;border-radius:3px}
.mock-logo{position:absolute;left:17px;top:20px;width:26px;height:26px;border-radius:6px;background:var(--lime)}
.mock-entry{position:absolute;left:150px;top:40px;font-size:22px;font-weight:600;color:#2a3550}
.mock-date{position:absolute;left:150px;top:82px;font-size:14px;color:#2a3550}
.mock-pill{position:absolute;left:330px;top:78px;padding:3px 14px;border-radius:12px;background:#44d18a;color:#fff;font-size:12px;font-weight:600}
.mock-card{position:absolute;top:130px;width:390px;height:470px;background:#fff;border:1px solid var(--line);border-radius:6px;padding:24px 22px}
.mock-stat{position:absolute;left:-10px;top:390px;width:200px;height:200px;background:#fff;border-radius:14px;box-shadow:0 14px 40px rgba(10,40,120,.25);padding:22px 24px}
.mock-stat b{font-size:24px;font-weight:500}
.mock-stat .up{font-size:12px;color:#3e7be0;margin-top:24px}
.mock-stat .go{margin-top:22px;width:150px;height:34px;border-radius:17px;background:#2f7ee8;color:#fff;font-size:12px;display:flex;align-items:center;justify-content:center}
.mock-wave{position:absolute;left:500px;top:500px;width:700px;height:300px;background:linear-gradient(160deg,#3a78d8,#0b3ca6);border-radius:40% 0 0 0;transform:rotate(14deg)}

/* Editor card */
.editor{position:absolute;width:446px;height:367px;background:var(--white);border:1px solid #e3e7ef;border-radius:4px;box-shadow:0 12px 30px rgba(20,40,90,.08);overflow:hidden}
.editor-head{position:absolute;left:38px;top:24px;display:flex;align-items:center;gap:14px;font-size:16px;color:#2a3147}
.toolbar{position:absolute;left:30px;top:75px;width:384px;height:84px;background:#f5f6f8;border:1px solid #d7dbe3;border-bottom:none;padding:12px 18px;font-size:14px;color:#333}
.toolbar .row{display:flex;align-items:center;gap:14px;height:26px}
.toolbar .fmt{font-family:Georgia,serif;font-weight:700;font-size:15px}
.toolbar .sel{width:100px}
.list-ico{width:15px;height:11px}
.content{position:absolute;left:43px;top:158px;width:360px;height:260px;border:1px solid #d7dbe3;background:#fff;padding:14px 12px 0 32px}
.content ul{font-size:18px;line-height:27px;color:#1f2430;list-style:none}
.content li{position:relative}
.content li::before{content:"•";position:absolute;left:-12px}

.feat-text{position:absolute;width:360px}
.feat-ico{width:62px;height:62px;border-radius:50%;background:var(--blue);display:flex;align-items:center;justify-content:center}
.feat-text h3{font-family:"Lexend",sans-serif;font-weight:400;font-size:26px;letter-spacing:-0.03em;color:#1b2340;margin-top:18px}
.feat-text p{font-size:13.5px;line-height:22px;color:var(--muted);margin-top:12px}
.dots{position:absolute;width:110px;height:110px;background:rgba(23,32,58,.03);border-radius:6px}

.section-title{position:absolute;left:0;width:1200px;text-align:center;font-size:46px;font-weight:400;color:#1a2136}
.section-title .hl{position:relative;display:inline-block}

/* AI band */
.ai{position:absolute;left:35px;top:2340px;width:1130px;height:301px;background:linear-gradient(100deg,#0b4fb0,#0c5cc0 60%,#0b4aa8);border-radius:2px}
.ai-visual{position:absolute;left:633px;top:2259px;width:483px;height:382px;border-radius:50% 50% 0 0/40% 40% 0 0;
  background:radial-gradient(ellipse at 70% 40%,#f2f4f8 0%,#c9ced8 40%,rgba(120,140,170,.5) 70%,rgba(20,70,170,0) 100%)}
.ai h2{position:absolute;left:90px;top:58px;font-size:48px;font-weight:500;color:#fff}
.ai h2 .hl{position:relative;display:inline-block}
.ai h4{position:absolute;left:90px;top:132px;font-family:"Lexend",sans-serif;font-weight:400;font-size:21px;letter-spacing:-0.03em;color:var(--lime)}
.ai p{position:absolute;left:90px;top:182px;width:420px;font-size:14px;line-height:22px;color:#e6eefc}
.ai p a{color:#fff;font-weight:700;text-decoration:underline}

/* Steps */
.step{position:absolute;top:2826px;width:320px;height:139px}
.step.card{background:#fff;border:1px solid #e4e8f0;border-radius:6px;box-shadow:0 10px 30px rgba(20,40,90,.07)}
.step-ico{position:absolute;top:34px;width:48px;height:48px;border-radius:50%;background:var(--blue);display:flex;align-items:center;justify-content:center}
.step h5{position:absolute;top:32px;font-family:"Lexend",sans-serif;font-weight:400;font-size:15px;letter-spacing:-0.02em;color:#1b2340}
.step p{position:absolute;top:60px;width:215px;font-size:11.5px;line-height:18px;color:var(--muted)}

/* Pricing */
.plan{position:absolute;top:3164px;width:292px;height:394px;background:#fff;border:1px solid #e6e9f0;border-radius:4px;text-align:center}
.plan .label{margin-top:28px;font-size:11px;font-weight:600;color:#9aa1b0;letter-spacing:.02em}
.plan .price{margin-top:12px;font-family:"Lexend",sans-serif;font-size:36px;font-weight:600;letter-spacing:-0.02em}
.plan .price small{font-size:13px;color:#1b2340;font-weight:500;letter-spacing:0}
.plan .tag{margin-top:6px;font-family:"Lexend",sans-serif;font-size:13.5px;color:#3a4257;letter-spacing:-0.02em}
.plan hr{border:none;border-top:1px solid #e9ecf2;margin:22px 28px 20px}
.plan ul{list-style:none;text-align:left;padding-left:26px;font-size:11.5px;color:#3a4257}
.plan li{height:27px;display:flex;align-items:center;gap:9px}
.plan li svg{width:10px;height:10px;flex:none}
.plan .choose{position:absolute;left:54px;top:323px;width:184px;height:43px;border-radius:3px;color:#fff;font-size:11.5px;font-weight:700;display:flex;align-items:center;justify-content:center}

/* Footer */
.footer{position:absolute;left:35px;top:3669px;width:1130px;height:404px;border-radius:4px;overflow:hidden;background:linear-gradient(120deg,#0a49ad,#0b4fb6 50%,#0a43a6)}
.footer-glow{position:absolute;left:-60px;top:50px;width:360px;height:360px;border-radius:50%;background:rgba(255,255,255,.05)}
.footer-brand{position:absolute;left:85px;top:153px;display:flex;align-items:center;gap:14px}
.footer-brand .sq{width:38px;height:38px;border-radius:8px;background:var(--lime)}
.footer-brand span{font-family:"Lexend",sans-serif;font-weight:600;font-size:40px;color:#fff;letter-spacing:-0.03em}
.fcol{position:absolute;top:72px;color:#fff}
.fcol h6{font-family:"Lexend",sans-serif;font-weight:400;font-size:21px;letter-spacing:-0.03em;margin-bottom:18px}
.fcol .link{font-size:12px;height:31.5px;display:flex;align-items:center;gap:8px;color:#e8effc}
.fcol .item{display:flex;gap:10px;font-size:12px;line-height:17px;color:#e8effc;margin-bottom:16px}
.fdiv{position:absolute;top:80px;width:1px;height:200px;background:rgba(255,255,255,.2)}
.social{display:flex;gap:12px}
.social span{width:51px;height:51px;border-radius:50%;background:rgba(255,255,255,.12);display:flex;align-items:center;justify-content:center;font-size:7.5px;color:#fff}
.fbottom{position:absolute;top:344px;font-size:12px;color:#e8effc}
.totop{position:absolute;left:1053px;top:331px;width:42px;height:42px;border-radius:50%;background:rgba(255,255,255,.15);display:flex;align-items:center;justify-content:center}
</style>
</head>
<body>

<!-- HERO -->
<header class="hero">
  <div class="mock" aria-label="App preview">
    <div class="mock-side">
      <div class="mock-logo"></div>
      <i style="top:80px"></i><i style="top:120px"></i><i style="top:160px"></i><i style="top:200px"></i>
    </div>
    <div class="mock-entry">Entry</div>
    <div class="mock-date">Thu Aug 22 2024 &#8964;</div>
    <div class="mock-pill">Gym</div>
    <div class="mock-card" style="left:110px">
      <div style="font-size:13px;color:#2a3550">What Went Well?</div>
      <div style="margin-top:22px;height:60px;background:#f5f6f8;border:1px solid #d7dbe3;font-size:11px;padding:10px">Normal &nbsp;&nbsp;&nbsp;&nbsp; <b>B</b> <i>I</i> <u>U</u> S</div>
      <ul style="border:1px solid #d7dbe3;padding:14px 14px 14px 28px;font-size:14px;line-height:20px;height:300px">
        <li>Completed all scheduled workouts this week.</li>
        <li>Increased bench press weight by 10 pounds.</li>
        <li>Maintained consistent energy levels throughout sessions.</li>
      </ul>
    </div>
    <div class="mock-card" style="left:540px;top:40px">
      <div style="font-size:13px;color:#2a3550">What Didn't Go Well?</div>
      <div style="margin-top:22px;height:60px;background:#f5f6f8;border:1px solid #d7dbe3;font-size:11px;padding:10px">Normal &nbsp;&nbsp;&nbsp;&nbsp; <b>B</b> <i>I</i> <u>U</u> S</div>
      <ul style="border:1px solid #d7dbe3;padding:14px 14px 14px 28px;font-size:14px;line-height:20px;height:300px">
        <li>Struggled with form on deadlifts, leading to lower back discomfort.</li>
        <li>Missed two stretching sessions after workouts.</li>
        <li>Skipped meal prep, resulting in inconsistent nutrition.</li>
      </ul>
    </div>
    <div class="mock-stat">
      <b>$71960</b>
      <div class="up">▲ 3600</div>
      <div class="go">Get Started</div>
      <div style="margin-top:26px;height:3px;width:150px;background:linear-gradient(90deg,#2f7ee8 20%,#e3e8f2 20%,#e3e8f2 60%,#2f7ee8 60%)"></div>
    </div>
  </div>

  <div class="brand"><div class="brand-mark"></div><div class="brand-name">Moodvane</div></div>
  <nav class="nav">
    <span style="left:0">Features &#8964;</span>
    <span style="left:86px">How it works</span>
    <span style="left:196px">Pricing</span>
    <span style="left:273px">Contact</span>
  </nav>
  <div class="btn-login">LOGIN</div>
  <div class="btn-signup">SIGNUP</div>

  <h1 class="hero-title display">Reflect,<br><span class="faint">Grow,</span> and<br>
    <span style="position:relative;display:inline-block">Succeed
      <svg class="swoosh" style="top:54px" viewBox="0 0 220 14" preserveAspectRatio="none"><path d="M6 8 Q110 -1 214 6" stroke="#a6e43a" stroke-width="3" fill="none" stroke-linecap="round"/><path d="M30 12 Q120 6 190 10" stroke="#a6e43a" stroke-width="2" fill="none" stroke-linecap="round"/></svg>
    </span></h1>
  <p class="hero-sub">Capture your journey with our intuitive journaling app designed to help you track progress &amp; plan for a better tomorrow.</p>
  <div class="hero-disc" role="img" aria-label="Stacked blue discs illustration"></div>
</header>

<!-- FEATURES -->
<h2 class="section-title display" style="top:905px">Our <span class="hl">Features<svg class="swoosh" style="top:52px" viewBox="0 0 200 14" preserveAspectRatio="none"><path d="M4 8 Q100 0 196 6" stroke="#a6e43a" stroke-width="3" fill="none" stroke-linecap="round"/><path d="M40 12 Q110 6 170 10" stroke="#a6e43a" stroke-width="2" fill="none"/></svg></span></h2>

<div class="dots" style="left:140px;top:983px" role="img" aria-label="Dot pattern"></div>
<div class="dots" style="left:953px;top:1395px" role="img" aria-label="Dot pattern"></div>
<div class="dots" style="left:140px;top:1810px" role="img" aria-label="Dot pattern"></div>

<article class="editor" style="left:188px;top:1031px">
  <div class="editor-head"><svg width="18" height="16" viewBox="0 0 18 16"><rect x="1" y="7" width="4" height="8" fill="#3b78d8"/><path d="M7 7 L10 1 Q12 1 12 4 L11 6 H16 Q17 7 16.5 9 L15 14 Q14.5 15 13 15 H7Z" fill="#3b78d8"/></svg>What Went Well?</div>
  <div class="toolbar">
    <div class="row"><span class="sel">Normal &nbsp;&nbsp;&nbsp;&nbsp;&nbsp;&nbsp;⇕</span><span class="fmt">B</span><span class="fmt"><i>I</i></span><span class="fmt"><u>U</u></span><span class="fmt"><s>S</s></span><span class="fmt">”</span></div>
    <div class="row"><svg class="list-ico" viewBox="0 0 15 11"><path d="M4 1.5H15M4 5.5H15M4 9.5H15M0 1.5H2M0 5.5H2M0 9.5H2" stroke="#333" stroke-width="1.4"/></svg><svg class="list-ico" viewBox="0 0 15 11"><path d="M4 1.5H15M4 5.5H15M4 9.5H15M0 1.5H2M0 5.5H2M0 9.5H2" stroke="#333" stroke-width="1.4"/></svg><svg class="list-ico" viewBox="0 0 15 11"><path d="M0 1H15M5 5.5H15M0 10H15M0 3.5L3 5.5 0 7.5" stroke="#333" stroke-width="1.4" fill="none"/></svg><svg class="list-ico" viewBox="0 0 15 11"><path d="M0 1H15M5 5.5H15M0 10H15M3 3.5L0 5.5 3 7.5" stroke="#333" stroke-width="1.4" fill="none"/></svg><span style="margin-left:20px"><i>T</i><sub>x</sub></span></div>
  </div>
  <div class="content"><ul>
    <li>Completed all scheduled workouts this week.</li>
    <li>Increased bench press weight by 10 pounds.</li>
    <li>Maintained consistent energy levels throughout sessions.</li>
  </ul></div>
</article>

<div class="feat-text" style="left:698px;top:1106px">
  <div class="feat-ico"><svg width="26" height="24" viewBox="0 0 18 16"><rect x="1" y="7" width="4" height="8" fill="#fff"/><path d="M7 7 L10 1 Q12 1 12 4 L11 6 H16 Q17 7 16.5 9 L15 14 Q14.5 15 13 15 H7Z" fill="#fff"/></svg></div>
  <h3>What Went Well</h3>
  <p>Document your achievements and what worked well. Reflect on your successes to stay motivated and inspired.</p>
</div>

<div class="feat-text" style="left:155px;top:1522px">
  <div class="feat-ico"><svg width="30" height="30" viewBox="0 0 30 30"><circle cx="15" cy="15" r="12" fill="#fff"/><circle cx="15" cy="15" r="9" fill="#0c4aa6"/><rect x="13.7" y="8.5" width="2.6" height="8" rx="1" fill="#fff"/><circle cx="15" cy="20" r="1.5" fill="#fff"/></svg></div>
  <h3>What Didn’t Go Well</h3>
  <p>Analyze what didn't go as planned. Understand your obstacles to turn setbacks into growth opportunities.</p>
</div>

<article class="editor" style="left:564px;top:1447px">
  <div class="editor-head"><svg width="17" height="15" viewBox="0 0 17 15"><path d="M8.5 0 L17 15 H0Z" fill="#3b78d8"/><rect x="7.7" y="5" width="1.6" height="5" fill="#fff"/><rect x="7.7" y="11.3" width="1.6" height="1.6" fill="#fff"/></svg>What Didn't Go Well?</div>
  <div class="toolbar">
    <div class="row"><span class="sel">Normal &nbsp;&nbsp;&nbsp;&nbsp;&nbsp;&nbsp;⇕</span><span class="fmt">B</span><span class="fmt"><i>I</i></span><span class="fmt"><u>U</u></span><span class="fmt"><s>S</s></span><span class="fmt">”</span></div>
    <div class="row"><svg class="list-ico" viewBox="0 0 15 11"><path d="M4 1.5H15M4 5.5H15M4 9.5H15M0 1.5H2M0 5.5H2M0 9.5H2" stroke="#333" stroke-width="1.4"/></svg><svg class="list-ico" viewBox="0 0 15 11"><path d="M4 1.5H15M4 5.5H15M4 9.5H15M0 1.5H2M0 5.5H2M0 9.5H2" stroke="#333" stroke-width="1.4"/></svg><svg class="list-ico" viewBox="0 0 15 11"><path d="M0 1H15M5 5.5H15M0 10H15M0 3.5L3 5.5 0 7.5" stroke="#333" stroke-width="1.4" fill="none"/></svg><svg class="list-ico" viewBox="0 0 15 11"><path d="M0 1H15M5 5.5H15M0 10H15M3 3.5L0 5.5 3 7.5" stroke="#333" stroke-width="1.4" fill="none"/></svg><span style="margin-left:20px"><i>T</i><sub>x</sub></span></div>
  </div>
  <div class="content"><ul>
    <li>Struggled with form on deadlifts, leading to lower back discomfort.</li>
    <li>Missed two stretching sessions after workouts.</li>
    <li>Skipped meal prep, resulting in inconsistent nutrition.</li>
  </ul></div>
</article>

<article class="editor" style="left:188px;top:1865px">
  <div class="editor-head" style="left:52px"><svg width="15" height="16" viewBox="0 0 15 16"><path d="M5 0H10V1H9V6L15 15H0L6 6V1H5Z" fill="#3b78d8"/></svg>Things To Try</div>
  <div class="toolbar" style="left:56px;width:344px;height:75px">
    <div class="row" style="height:22px;font-size:13px"><span class="sel" style="width:95px">Normal &nbsp;&nbsp;&nbsp;&nbsp;&nbsp;⇕</span><span class="fmt">B</span><span class="fmt"><i>I</i></span><span class="fmt"><u>U</u></span><span class="fmt"><s>S</s></span><span class="fmt">”</span></div>
    <div class="row" style="height:22px"><svg class="list-ico" viewBox="0 0 15 11"><path d="M4 1.5H15M4 5.5H15M4 9.5H15M0 1.5H2M0 5.5H2M0 9.5H2" stroke="#333" stroke-width="1.4"/></svg><svg class="list-ico" viewBox="0 0 15 11"><path d="M4 1.5H15M4 5.5H15M4 9.5H15M0 1.5H2M0 5.5H2M0 9.5H2" stroke="#333" stroke-width="1.4"/></svg><svg class="list-ico" viewBox="0 0 15 11"><path d="M0 1H15M5 5.5H15M0 10H15M0 3.5L3 5.5 0 7.5" stroke="#333" stroke-width="1.4" fill="none"/></svg><svg class="list-ico" viewBox="0 0 15 11"><path d="M0 1H15M5 5.5H15M0 10H15M3 3.5L0 5.5 3 7.5" stroke="#333" stroke-width="1.4" fill="none"/></svg><span style="margin-left:20px"><i>T</i><sub>x</sub></span></div>
  </div>
  <div class="content" style="left:56px;top:149px;width:344px;padding:12px 10px 0 30px"><ul style="font-size:16.5px;line-height:25px">
    <li>Focus on deadlift form by lowering the weight and reviewing proper technique.</li>
    <li>Set reminders for post-workout stretching to prevent muscle tightness.</li>
    <li>Dedicate Sunday evenings to meal prep to ensure a balanced diet.</li>
  </ul></div>
</article>

<div class="feat-text" style="left:698px;top:1941px">
  <div class="feat-ico" style="background:var(--soft-blue)"><svg width="24" height="26" viewBox="0 0 15 16"><path d="M5 0H10V1H9V6L15 15H0L6 6V1H5Z" fill="none" stroke="#fff" stroke-width="1.3"/><path d="M3 11H12L14 14.5H1Z" fill="#fff"/></svg></div>
  <h3>Things To Try</h3>
  <p>Identify new strategies and actions to try. Set goals and track your progress towards continuous improvement.</p>
</div>

<!-- AI COACH -->
<section class="ai">
  <h2 class="display">AI Coach <span class="hl">Preview<svg class="swoosh" style="top:48px" viewBox="0 0 200 14" preserveAspectRatio="none"><path d="M4 8 Q100 0 196 6" stroke="#a6e43a" stroke-width="3" fill="none" stroke-linecap="round"/><path d="M40 12 Q110 6 170 10" stroke="#a6e43a" stroke-width="2" fill="none"/></svg></span></h2>
  <h4>Meet Your Future AI Coach</h4>
  <p>Unlock personalized insights and actionable advice based on your journaling history. <a>Coming soon</a> to guide you towards your goals.</p>
</section>
<div class="ai-visual" role="img" aria-label="Silver humanoid robot raising its hand"></div>

<!-- HOW IT WORKS -->
<h2 class="section-title display" style="top:2726px">How It <span class="hl">Works<svg class="swoosh" style="top:52px" viewBox="0 0 200 14" preserveAspectRatio="none"><path d="M4 8 Q100 0 196 6" stroke="#a6e43a" stroke-width="3" fill="none" stroke-linecap="round"/><path d="M40 12 Q110 6 170 10" stroke="#a6e43a" stroke-width="2" fill="none"/></svg></span></h2>

<div class="step" style="left:100px">
  <div class="step-ico" style="left:15px"><svg width="22" height="22" viewBox="0 0 22 22"><path d="M4 2H14L18 6V20H4Z" fill="#fff"/><path d="M9 15L10 11L17 4L20 7L13 14Z" fill="#0c4aa6" stroke="#fff" stroke-width="1"/></svg></div>
  <h5 style="left:80px">Start a New Journal Entry</h5>
  <p style="left:80px">Begin by documenting what went well, what didn't, and what you plan to try.</p>
</div>
<div class="step card" style="left:448px">
  <div class="step-ico" style="left:27px"><svg width="22" height="18" viewBox="0 0 22 18"><path d="M1 2L9 9L1 16Z M21 2L13 9L21 16Z" fill="#fff"/><rect x="10" y="0" width="2" height="18" fill="#fff"/></svg></div>
  <h5 style="left:92px">Reflect and Analyze</h5>
  <p style="left:92px">Review your entries to gain insights and identify patterns over time.</p>
</div>
<div class="step" style="left:800px">
  <div class="step-ico" style="left:27px;background:var(--soft-blue)"><svg width="24" height="24" viewBox="0 0 24 24"><circle cx="12" cy="12" r="7" fill="none" stroke="#fff" stroke-width="3" stroke-dasharray="3 2.5"/><circle cx="12" cy="12" r="5" fill="#fff"/><circle cx="12" cy="12" r="2.5" fill="#8bb2e2"/></svg></div>
  <h5 style="left:93px">Take Action</h5>
  <p style="left:93px">Use your reflections to make informed decisions and set new goals.</p>
</div>

<!-- PRICING -->
<h2 class="section-title display" style="top:3068px">Pricing or <span class="hl">Signup<svg class="swoosh" style="top:52px" viewBox="0 0 200 14" preserveAspectRatio="none"><path d="M4 8 Q100 0 196 6" stroke="#a6e43a" stroke-width="3" fill="none" stroke-linecap="round"/><path d="M40 12 Q110 6 170 10" stroke="#a6e43a" stroke-width="2" fill="none"/></svg></span></h2>

<div class="plan" style="left:142px">
  <div class="label">FREE PLAN</div>
  <div class="price" style="color:var(--blue)">$0<small>/Month</small></div>
  <div class="tag">Start Journaling Today</div>
  <hr>
  <ul>
    <li><svg viewBox="0 0 10 10"><path d="M1 5L4 8L9 2" stroke="#9aa1b0" stroke-width="1.4" fill="none"/></svg>Access to core journaling tools</li>
    <li><svg viewBox="0 0 10 10"><path d="M1 5L4 8L9 2" stroke="#9aa1b0" stroke-width="1.4" fill="none"/></svg>Basic retrospective board with</li>
    <li><svg viewBox="0 0 10 10"><path d="M1 5L4 8L9 2" stroke="#9aa1b0" stroke-width="1.4" fill="none"/></svg>Limited entry history</li>
  </ul>
  <div class="choose" style="background:var(--blue)">CHOOSE YOUR PLAN</div>
</div>
<div class="plan" style="left:454px">
  <div class="label">PRO PLAN</div>
  <div class="price" style="color:var(--sky)">14.99<small>/Month</small></div>
  <div class="tag">Unlock Enhanced Features</div>
  <hr>
  <ul>
    <li><svg viewBox="0 0 10 10"><path d="M1 5L4 8L9 2" stroke="#9aa1b0" stroke-width="1.4" fill="none"/></svg>All Free Plan features</li>
    <li><svg viewBox="0 0 10 10"><path d="M1 5L4 8L9 2" stroke="#9aa1b0" stroke-width="1.4" fill="none"/></svg>Unlimited entry history</li>
    <li><svg viewBox="0 0 10 10"><path d="M1 5L4 8L9 2" stroke="#9aa1b0" stroke-width="1.4" fill="none"/></svg>Advanced analytics and insights</li>
    <li><svg viewBox="0 0 10 10"><path d="M1 5L4 8L9 2" stroke="#9aa1b0" stroke-width="1.4" fill="none"/></svg>Customizable templates</li>
  </ul>
  <div class="choose" style="background:#0b5cb8">CHOOSE YOUR PLAN</div>
</div>
<div class="plan" style="left:765px">
  <div class="label">PREMIUM PLAN</div>
  <div class="price" style="color:#6a9ed6">$17.99<small>/Month</small></div>
  <div class="tag">Experience the Full Potential</div>
  <hr>
  <ul>
    <li><svg viewBox="0 0 10 10"><path d="M1 5L4 8L9 2" stroke="#9aa1b0" stroke-width="1.4" fill="none"/></svg>All Pro Plan features</li>
    <li><svg viewBox="0 0 10 10"><path d="M1 5L4 8L9 2" stroke="#9aa1b0" stroke-width="1.4" fill="none"/></svg>Priority access to the AI coach</li>
    <li><svg viewBox="0 0 10 10"><path d="M1 5L4 8L9 2" stroke="#9aa1b0" stroke-width="1.4" fill="none"/></svg>Premium support and resources</li>
    <li><svg viewBox="0 0 10 10"><path d="M1 5L4 8L9 2" stroke="#9aa1b0" stroke-width="1.4" fill="none"/></svg>Early access to new features</li>
  </ul>
  <div class="choose" style="background:var(--soft-blue)">CHOOSE YOUR PLAN</div>
</div>

<!-- FOOTER -->
<footer class="footer">
  <div class="footer-glow"></div>
  <div class="footer-brand"><div class="sq"></div><span>Moodvane</span></div>

  <div class="fcol" style="left:414px">
    <h6>Quick Links</h6>
    <div class="link">› Features</div>
    <div class="link">› How it works</div>
    <div class="link">› Benefits</div>
    <div class="link">› Pricing</div>
    <div class="link">› Contact</div>
  </div>
  <div class="fdiv" style="left:571px"></div>
  <div class="fcol" style="left:606px">
    <h6>Contact Us</h6>
    <div class="item"><svg width="12" height="10" viewBox="0 0 12 10"><rect width="12" height="10" rx="1" fill="#fff"/><path d="M0 1L6 6L12 1" stroke="#0a49ad" fill="none"/></svg><div>Email:<br>hello@moodvane-mail.com</div></div>
    <div class="item"><svg width="12" height="12" viewBox="0 0 12 12"><path d="M2 0L5 3L3.5 4.5Q5 7.5 7.5 8.5L9 7L12 10L10 12Q3 11 0 2Z" fill="#fff"/></svg><div>Phone:<br>+08 123 456 7890</div></div>
    <div class="item"><svg width="12" height="14" viewBox="0 0 12 14"><path d="M6 14Q0 7 0 6A6 6 0 0 1 12 6Q12 7 6 14Z" fill="#fff"/><circle cx="6" cy="6" r="2.2" fill="#0a49ad"/></svg><div>Location:<br>Some address line here<br>United Kingdom</div></div>
  </div>
  <div class="fdiv" style="left:826px"></div>
  <div class="fcol" style="left:872px">
    <h6>Follow Us</h6>
    <div class="social"><span>Friendloop</span><span>Chirpline</span><span>Searchly</span></div>
  </div>

  <div class="fbottom" style="left:93px">© Copyright 2024, All Rights Reserved</div>
  <div class="fbottom" style="left:790px">Privacy Policy | Terms of Service</div>
  <div class="totop"><svg width="12" height="14" viewBox="0 0 12 14"><path d="M6 14V1M1 6L6 1L11 6" stroke="#fff" stroke-width="1.5" fill="none"/></svg></div>
</footer>

</body>
</html>
```